I need to refresh my meeting minutes pages (2 of them)

I have 2 pages that need to be modernized with a new look and feel. I have attached the 2 pages that need the refresh. I am okay with one page submissions as long as the winner is willing to add the second page before payment :-) Any questions please let me know. The logo on the page is not ours but a sample of what client may give us.

```html
<!DOCTYPE html>
<html lang="en">
<head>
<meta charset="utf-8">
<title>Meetings – Regular Meeting Agenda</title>
<link href="https://fonts.googleapis.com/css2?family=Albert+Sans:wght@400;500;600&display=swap" rel="stylesheet">
<style>
  :root{
    --blue:#2f7cf0;
    --blue-soft:#bcd7f7;
    --page:#f0f2f6;
    --card:#ffffff;
    --tile:#f1f3f6;
    --ink:#1d1f24;
    --muted:#5d6168;
    --line:#dde1e7;
  }
  *{box-sizing:border-box;margin:0;padding:0}
  html,body{width:1200px;height:569px;overflow:hidden}
  body{background:var(--page);font-family:"Albert Sans",sans-serif;color:var(--ink);position:relative}
  .topbar{position:absolute;left:0;top:0;width:1200px;height:39px;background:#f7f9fb;border-bottom:2px solid var(--blue)}
  .brand{position:absolute;left:12px;top:11px;font-size:13px;font-weight:600;color:var(--blue)}
  .nav{position:absolute;left:893px;top:0;height:37px;display:flex}
  .nav a{display:block;height:37px;line-height:37px;font-size:8.8px;color:var(--ink);text-decoration:none;text-align:center;white-space:nowrap}
  .nav a.active{background:var(--blue);color:#fff}

  .search{position:absolute;left:12.5px;top:58px;width:275px;height:31px;background:var(--card);border:1px solid var(--line);border-radius:2px}
  .search span{position:absolute;left:12px;top:9px;font-size:9px;color:#333}
  .search svg{position:absolute;right:11px;top:8px}
  .side-rule{position:absolute;left:12.5px;top:102px;width:275px;height:1px;background:var(--line)}

  .group{position:absolute;left:12.5px;width:275px;background:var(--card);border-radius:2px}
  .group-head{position:relative;height:31px}
  .group-icon{position:absolute;left:6px;top:6px;width:19px;height:19px;border-radius:3px;background:var(--blue)}
  .group-icon svg{position:absolute;left:4px;top:4px}
  .group-title{position:absolute;left:39px;top:10px;font-size:9.5px}
  .group-toggle{position:absolute;right:7px;top:8px;font-size:11px}
  .featured{top:115px;height:31px}
  .year{top:159px;height:397px}
  .year .group-head{border-bottom:1px solid var(--line);margin:0 6px;height:31px}
  .year .group-icon{left:0}
  .year .group-title{left:33px}
  .year .group-toggle{right:1px}

  .meeting{position:absolute;left:6px;width:262px;height:44px;background:var(--tile);border-radius:2px}
  .meeting .kind{position:absolute;left:9px;top:9px;font-size:8.3px;color:var(--muted)}
  .meeting .date{position:absolute;left:9px;top:23px;font-size:10px;font-weight:500}
  .meeting .time{position:absolute;right:10px;top:9px;font-size:8px;color:var(--muted);display:flex;align-items:center;gap:5px}
  .meeting.current{box-shadow:inset 2px 0 0 var(--blue)}
  .meeting.special{background:var(--blue-soft)}
  .meeting.special .kind{left:24px}
  .meeting.special .star{position:absolute;left:9px;top:10px}

  .pager{position:absolute;top:58px;width:31px;height:31px;background:var(--card);border-radius:2px}
  .pager svg{position:absolute;left:9px;top:9px}
  .prev{left:319px}.next{left:356px}.share{left:1156px}

  .detail{position:absolute;left:319px;top:102.5px;width:868px;height:453.5px;background:var(--card);border-radius:2px}
  .detail h1{position:absolute;left:18.5px;top:22px;font-size:15px;font-weight:400}
  .meta{position:absolute;left:19px;top:46px;display:flex;align-items:center;font-size:10px}
  .meta .clock{margin-left:12px;font-size:8px;color:var(--muted);display:flex;align-items:center;gap:5px}
  .detail .rule{position:absolute;left:18.5px;top:76.5px;width:831px;height:1px;background:var(--line)}
  .venue{position:absolute;left:20px;top:96.5px;width:213px;height:69px;background:var(--tile);border-radius:2px}
  .venue svg{position:absolute;left:13px;top:31px}
  .venue p{position:absolute;left:38px;top:13px;font-size:9.3px;line-height:15px;white-space:nowrap}
  .venue strong{font-weight:500}
  .note{position:absolute;left:20px;top:182px;font-size:8.2px}
  .actions{position:absolute;left:18.5px;top:391.5px;display:flex;gap:12.5px}
  .action{height:38px;background:var(--tile);border-radius:2px;display:flex;align-items:center;padding:0 17px 0 12px;gap:12px;font-size:9.5px;font-weight:500}
</style>
</head>
<body>
  <header class="topbar">
    <div class="brand">Brookfield Schools</div>
    <nav class="nav">
      <a href="#" style="width:86px">FEATURED</a>
      <a href="#" class="active" style="width:67px">MEETINGS</a>
      <a href="#" style="width:80px">AGENDA</a>
      <a href="#" style="width:60px">POLICIES</a>
    </nav>
  </header>

  <div class="search">
    <span>Search meetings...</span>
    <svg width="13" height="13" viewBox="0 0 13 13"><circle cx="5.5" cy="5.5" r="4.3" fill="none" stroke="#2f7cf0" stroke-width="1.6"/><line x1="8.7" y1="8.7" x2="12" y2="12" stroke="#2f7cf0" stroke-width="1.8" stroke-linecap="round"/></svg>
  </div>
  <div class="side-rule"></div>

  <section class="group featured">
    <div class="group-head">
      <div class="group-icon"><svg width="11" height="11" viewBox="0 0 24 24"><path fill="#fff" d="M12 2l3 6.6 7.2.8-5.4 4.9 1.5 7.1L12 17.8 5.7 21.4l1.5-7.1L1.8 9.4 9 8.6z"/></svg></div>
      <div class="group-title">FEATURED</div>
      <div class="group-toggle">+</div>
    </div>
  </section>

  <section class="group year">
    <div class="group-head">
      <div class="group-icon"><svg width="11" height="11" viewBox="0 0 12 12"><rect x="1" y="2" width="10" height="9" rx="1" fill="#fff"/><rect x="2.5" y="5" width="7" height="4.5" fill="#2f7cf0"/><rect x="3" y="0.5" width="1.4" height="3" fill="#fff"/><rect x="7.6" y="0.5" width="1.4" height="3" fill="#fff"/></svg></div>
      <div class="group-title">2025</div>
      <div class="group-toggle">–</div>
    </div>

    <div class="meeting current" style="top:44px"><span class="kind">Regular Meeting Agenda</span><span class="date">May 05, 2025 (Monday)</span><span class="time">6:00 PM <svg width="9" height="9" viewBox="0 0 10 10"><circle cx="5" cy="5" r="4.2" fill="none" stroke="#444" stroke-width="1"/><path d="M5 2.5V5l1.6 1" fill="none" stroke="#444" stroke-width="1"/></svg></span></div>
    <div class="meeting" style="top:94px"><span class="kind">Regular Meeting Agenda</span><span class="date">May 05, 2025 (Monday)</span><span class="time">6:00 PM <svg width="9" height="9" viewBox="0 0 10 10"><circle cx="5" cy="5" r="4.2" fill="none" stroke="#444" stroke-width="1"/><path d="M5 2.5V5l1.6 1" fill="none" stroke="#444" stroke-width="1"/></svg></span></div>
    <div class="meeting special" style="top:144px"><svg class="star" width="10" height="10" viewBox="0 0 24 24"><path fill="#2f7cf0" d="M12 2l3 6.6 7.2.8-5.4 4.9 1.5 7.1L12 17.8 5.7 21.4l1.5-7.1L1.8 9.4 9 8.6z"/></svg><span class="kind">Special Meeting Agenda</span><span class="date">May 05, 2025 (Monday)</span><span class="time">6:00 PM <svg width="9" height="9" viewBox="0 0 10 10"><circle cx="5" cy="5" r="4.2" fill="none" stroke="#444" stroke-width="1"/><path d="M5 2.5V5l1.6 1" fill="none" stroke="#444" stroke-width="1"/></svg></span></div>
    <div class="meeting" style="top:194px"><span class="kind">Regular Meeting Agenda</span><span class="date">May 05, 2025 (Monday)</span><span class="time">6:00 PM <svg width="9" height="9" viewBox="0 0 10 10"><circle cx="5" cy="5" r="4.2" fill="none" stroke="#444" stroke-width="1"/><path d="M5 2.5V5l1.6 1" fill="none" stroke="#444" stroke-width="1"/></svg></span></div>
    <div class="meeting" style="top:244px"><span class="kind">Regular Meeting Agenda</span><span class="date">May 05, 2025 (Monday)</span><span class="time">6:00 PM <svg width="9" height="9" viewBox="0 0 10 10"><circle cx="5" cy="5" r="4.2" fill="none" stroke="#444" stroke-width="1"/><path d="M5 2.5V5l1.6 1" fill="none" stroke="#444" stroke-width="1"/></svg></span></div>
    <div class="meeting" style="top:294px"><span class="kind">Regular Meeting Agenda</span><span class="date">May 05, 2025 (Monday)</span><span class="time">6:00 PM <svg width="9" height="9" viewBox="0 0 10 10"><circle cx="5" cy="5" r="4.2" fill="none" stroke="#444" stroke-width="1"/><path d="M5 2.5V5l1.6 1" fill="none" stroke="#444" stroke-width="1"/></svg></span></div>
    <div class="meeting" style="top:344px"><span class="kind">Regular Meeting Agenda</span><span class="date">May 05, 2025 (Monday)</span><span class="time">6:00 PM <svg width="9" height="9" viewBox="0 0 10 10"><circle cx="5" cy="5" r="4.2" fill="none" stroke="#444" stroke-width="1"/><path d="M5 2.5V5l1.6 1" fill="none" stroke="#444" stroke-width="1"/></svg></span></div>
  </section>

  <div class="pager prev"><svg width="13" height="13" viewBox="0 0 13 13"><path d="M8.5 2L4 6.5 8.5 11" fill="none" stroke="#111" stroke-width="1.8" stroke-linecap="round" stroke-linejoin="round"/></svg></div>
  <div class="pager next"><svg width="13" height="13" viewBox="0 0 13 13"><path d="M4.5 2L9 6.5 4.5 11" fill="none" stroke="#111" stroke-width="1.8" stroke-linecap="round" stroke-linejoin="round"/></svg></div>
  <div class="pager share"><svg width="13" height="13" viewBox="0 0 13 13"><circle cx="10" cy="2.8" r="2.3" fill="#2f7cf0"/><circle cx="3" cy="6.5" r="2.3" fill="#2f7cf0"/><circle cx="10" cy="10.2" r="2.3" fill="#2f7cf0"/><path d="M10 2.8L3 6.5 10 10.2" fill="none" stroke="#2f7cf0" stroke-width="1.4"/></svg></div>

  <main class="detail">
    <h1>Regular Meeting Agenda</h1>
    <div class="meta">May 05, 2025 (Monday)<span class="clock">6:00 PM <svg width="9" height="9" viewBox="0 0 10 10"><circle cx="5" cy="5" r="4.2" fill="none" stroke="#555" stroke-width="1"/><path d="M5 2.5V5l1.6 1" fill="none" stroke="#555" stroke-width="1"/></svg></span></div>
    <div class="rule"></div>

    <div class="venue">
      <svg width="12" height="16" viewBox="0 0 12 16"><path d="M6 0a6 6 0 0 0-6 6c0 4.5 6 10 6 10s6-5.5 6-10a6 6 0 0 0-6-6z" fill="#2f7cf0"/><circle cx="6" cy="6" r="2.2" fill="#f1f3f6"/></svg>
      <p><strong>Ashgrove High School Media Center</strong><br>1480 North Maple Grove Road<br>Harlow Crest, Westmere 00000</p>
    </div>

    <p class="note">This meeting is a meeting of the Board of Education in public for the purpose of conducting the District’s business. There is a time for public participation during the meeting as indicated in the agenda.</p>

    <div class="actions">
      <div class="action" style="width:131px">
        <svg width="15" height="13" viewBox="0 0 15 13"><g fill="#2f7cf0"><circle cx="1.5" cy="1.5" r="1.4"/><circle cx="1.5" cy="6.5" r="1.4"/><circle cx="1.5" cy="11.5" r="1.4"/><rect x="4.5" y="0.7" width="10" height="1.6" rx=".8"/><rect x="4.5" y="5.7" width="10" height="1.6" rx=".8"/><rect x="4.5" y="10.7" width="10" height="1.6" rx=".8"/></g></svg>
        View the Agenda
      </div>
      <div class="action" style="width:170px">
        <svg width="15" height="16" viewBox="0 0 15 16"><path d="M1 0h7l4 4v12H1z" fill="#2f7cf0"/><path d="M8 0v4h4" fill="#9cc0f6"/><rect x="5" y="9.5" width="10" height="6" fill="#fff"/><text x="5.5" y="15" font-size="5.5" font-family="Albert Sans,sans-serif" font-weight="600" fill="#2f7cf0">PDF</text></svg>
        Download Agenda as PDF
      </div>
      <div class="action" style="width:130px">
        <svg width="15" height="15" viewBox="0 0 15 15"><rect x="3.5" y="0.5" width="8" height="4" rx="1" fill="none" stroke="#2f7cf0" stroke-width="1.4"/><rect x="0.5" y="4.5" width="14" height="6.5" rx="2" fill="#2f7cf0"/><rect x="3.5" y="8.5" width="8" height="6" rx="1" fill="#fff" stroke="#2f7cf0" stroke-width="1.4"/></svg>
        Print the Agenda
      </div>
    </div>
  </main>
</body>
</html>
```